Popcorn Bag design

We need package design for the launch of our popcorn. We have chosen Hawaiian salts - Red and Black Lava - as our salts. Based on that decision we want to take a bit of a aloha spirit on the bag. Not over the top, but clearly a Hawaiian feel.. Required a Big Kahuna, smiling and with one arm out with a hang loose hand. The basic design will be used for multiple flavors of popcorn and a larger and smaller bags.
Please see the attached word document with more information.
Popcorn flavors for the design
Alaea Hawaiian Red Sea Salt
Alaea Hawaiian Red Sea Salt and Black Pepper
Black Hawaiian Lava Salt on Blue Kernels
The winning design will include the following
Design for the overall package - front and back (we have provided some information for the front and back of the bag.
Big Kahuna (smiling, with one arm out showing the "hang loose" hand samples. File(s) attached.
We will upload our logo, nutrition label and other
The winner will provide the following files:
Front and back of design - artwork ready
Front transparent background
Back transparent background
Big Kahuna transparent background

```html
<!DOCTYPE html>
<html lang="en">
<head>
<meta charset="utf-8">
<title>Kernel Cove Popcorn – Alaea Hawaiian Red Sea Salt</title>
<link href="https://fonts.googleapis.com/css2?family=Asap+Condensed:ital,wght@0,400;0,500;0,700;1,500&family=Yellowtail&display=swap" rel="stylesheet">
<style>
  :root {
    --navy: #1f2a44;
    --red: #e5222e;
    --stripe-light: #f5f4f1;
    --stripe-grey: #aab1be;
    --paper: #fbfbfa;
    --stage: #eceef1;
    --muted: #c9ced8;
    --kernel-light: #f7f1e0;
  }
  * { box-sizing: border-box; margin: 0; padding: 0; }
  html, body { width: 900px; height: 1200px; overflow: hidden; background: var(--stage); }
  body { position: relative; font-family: "Asap Condensed", sans-serif; color: var(--navy); }

  .bag-front {
    position: absolute; left: 72px; top: 40px; width: 755px; height: 1120px;
    overflow: hidden;
    background: repeating-linear-gradient(90deg,
      var(--stripe-light) 0 46px, var(--stripe-grey) 46px 92px);
  }
  .brand-panel {
    position: absolute; left: 160px; top: 0; width: 435px; height: 390px;
    background: var(--paper);
    border-left: 8px solid var(--navy); border-right: 8px solid var(--navy);
    overflow: hidden;
  }
  .brand-name {
    position: absolute; left: 0; right: 0; top: 78px; text-align: center;
    font-weight: 700; font-size: 66px; letter-spacing: 2px; color: var(--red);
    line-height: 1; white-space: nowrap;
  }
  .product-word {
    position: absolute; left: 0; right: 0; top: 170px; text-align: center;
    font-weight: 700; font-size: 96px; letter-spacing: 1px; color: var(--navy);
    line-height: 1; white-space: nowrap;
  }
  .tagline {
    position: absolute; left: 365px; top: 372px; width: 240px;
    font-family: "Yellowtail", "Brush Script MT", cursive; font-size: 38px; line-height: 0.95;
    color: var(--red); transform: rotate(-9deg); text-align: center;
  }
  .flavor-band {
    position: absolute; left: 290px; top: 477px; width: 465px; height: 48px;
    background: var(--navy); border-radius: 26px 0 0 0;
    color: #fff; font-style: italic; font-weight: 500; font-size: 27px;
    line-height: 48px; padding-left: 62px; white-space: nowrap;
  }
  .band-rule {
    position: absolute; left: 60px; top: 522px; width: 695px; height: 6px;
    background: var(--navy);
  }
  .popcorn-photo {
    position: absolute; left: 265px; top: 528px; width: 445px; height: 318px;
    background: radial-gradient(ellipse at 55% 62%, var(--kernel-light) 0 45%, #efe3c4 62%, var(--paper) 78%);
  }
  .mascot-art {
    position: absolute; left: 62px; top: 478px; width: 212px; height: 382px;
    background: linear-gradient(180deg, #2c3a5c, var(--navy));
    border-radius: 90px 90px 18px 18px;
  }
  .approval-badge {
    position: absolute; left: 72px; top: 850px; width: 190px; height: 140px;
    background: var(--navy); border-radius: 0 0 95px 95px;
    color: #fff; text-align: center; font-size: 25px; line-height: 31px;
    padding-top: 54px;
  }
  .benefits {
    position: absolute; left: 280px; top: 848px; width: 475px; height: 132px;
    background: var(--navy); border-radius: 0 0 0 70px;
    list-style: none; padding: 14px 0 0 98px; color: #fff;
    font-weight: 500; font-size: 29px; line-height: 36px; white-space: nowrap;
  }
  .benefits li { display: flex; align-items: center; gap: 10px; }
  .benefits svg { width: 26px; height: 26px; flex: none; }
  .claims {
    position: absolute; left: 50px; top: 1008px; width: 210px;
    text-align: center; font-size: 25px; color: var(--navy);
  }
  .claims p { padding: 4px 0; border-top: 1px solid #9aa1af; }
  .claims p:first-child { font-style: italic; }
  .claims p:last-child { border-bottom: 1px solid #9aa1af; }
  .net-weight {
    position: absolute; left: 437px; top: 1013px; width: 256px; height: 140px;
    background: var(--navy); border-radius: 128px 128px 0 0;
    color: var(--muted); text-align: center; font-size: 25px; line-height: 30px;
    padding-top: 28px;
  }
</style>
</head>
<body>
  <main class="bag-front">
    <section class="brand-panel">
      <div class="brand-name">KERNEL COVE</div>
      <div class="product-word">POPCORN</div>
    </section>
    <div class="tagline">Taste The Difference</div>

    <div class="popcorn-photo" role="img" aria-label="Photo of a heap of freshly popped white popcorn"></div>
    <div class="band-rule"></div>
    <div class="flavor-band">Alaea Hawaiian Red Sea Salt</div>

    <div class="mascot-art" role="img" aria-label="Illustration of the Big Kahuna tiki mascot in navy tones"></div>
    <div class="approval-badge">Big Kahuna<br>Approved</div>

    <ul class="benefits">
      <li><svg viewBox="0 0 26 26"><circle cx="13" cy="13" r="12" fill="#fff"/><path d="M7 13.5l4 4 8-9" fill="none" stroke="#1f2a44" stroke-width="3" stroke-linecap="round" stroke-linejoin="round"/></svg>Naturally lower in sodium</li>
      <li><svg viewBox="0 0 26 26"><circle cx="13" cy="13" r="12" fill="#fff"/><path d="M7 13.5l4 4 8-9" fill="none" stroke="#1f2a44" stroke-width="3" stroke-linecap="round" stroke-linejoin="round"/></svg>Higher in iron</li>
      <li><svg viewBox="0 0 26 26"><circle cx="13" cy="13" r="12" fill="#fff"/><path d="M7 13.5l4 4 8-9" fill="none" stroke="#1f2a44" stroke-width="3" stroke-linecap="round" stroke-linejoin="round"/></svg>Smooth rich flavor</li>
    </ul>

    <div class="claims">
      <p>Popped with Aloha</p>
      <p>Gluten Free</p>
    </div>

    <div class="net-weight">Net weight<br>4.4oz</div>
  </main>
</body>
</html>
```